Talent Management Company Needs Business Cards

Using one of the logos provided (attached) K&R Talent Collective needs a business card designed.
Please visit our website for more information about us-

www.krtalentcollective.example

The face should feature a dramatic presentation of the logo with the back being reserved for our professional information which is:

The information should be:
Dorian T. Vickers
C.E.O
Email: dtvickers@krtalentcollective.example
Mobile: 555-804-2917
Website: www.krtalentcollective.example

Marcus L. Vickers
Director of Public Relations
Email: mlvickers@krtalentcollective.example
Mobile: 555-806-3350

Jules R. Hampton
Director of Client Development
Email: jhampton@krtalentcollective.example

Simon Hurlock
Director of Brand Development
Email: shurlock@krtalentcollective.example

Would like the logo to have color. I would like to see one side red or black and the other side white but if it looks better in either black or red that would be fine to but would like to see how it comes out.

Please feel free to message me and if you would like just the icon alone I have other image files that I can send as well.

Target Market(s)

Professional Athletes, coaches, entertainers age 18-35 but also must be accepted in the business community

Industry/Entity Type

Business

Requirements
Must have
• 1) Use the logo
2) Double sided
3) Distinctive
Nice to have
• Small simple images for telephone, e-mail, and Url.

```html
<!DOCTYPE html>
<html lang="en">
<head>
<meta charset="utf-8">
<title>K&amp;R Talent Collective — Business Card</title>
<link rel="stylesheet" href="https://fonts.googleapis.com/css2?family=Source+Sans+3:wght@400;600;700&display=swap">
<style>
  :root {
    --backdrop: #e9e6e2;
    --card-black: #0b0b0b;
    --card-black-soft: #1e1e1e;
    --brand-red: #b3141c;
    --brand-red-deep: #6e0a10;
    --brand-red-bright: #d3202a;
    --silver-light: #f2f2f2;
    --silver-dark: #8c8c8c;
    --ink-light: #ffffff;
  }
  * { box-sizing: border-box; margin: 0; padding: 0; }
  html, body { width: 1200px; height: 665px; overflow: hidden; }
  body {
    background: var(--backdrop);
    font-family: "Source Sans 3", sans-serif;
    position: relative;
  }
  .card {
    position: absolute;
    top: 178px;
    width: 530px;
    height: 310px;
    border-radius: 28px;
    overflow: hidden;
    color: var(--ink-light);
    box-shadow: 0 6px 18px rgba(0,0,0,0.18);
  }
  .card--contact { left: 50px; background: var(--card-black); }
  .card--brand {
    left: 620px;
    background: radial-gradient(ellipse at 45% 40%, var(--brand-red-bright) 0%, var(--brand-red) 40%, var(--brand-red-deep) 100%);
  }
  .card__bands { position: absolute; inset: 0; width: 100%; height: 100%; }

  .holder { position: absolute; top: 20px; right: 30px; text-align: right; }
  .holder__name { font-weight: 700; font-size: 19px; line-height: 1.1; }
  .holder__title { font-size: 12px; letter-spacing: 0.5px; }

  .wordmark {
    position: absolute; top: 88px; left: 0; width: 100%;
    display: flex; align-items: center; justify-content: center; gap: 12px;
  }
  .wordmark__square { width: 18px; height: 18px; background: var(--brand-red-bright); }
  .wordmark__name {
    font-weight: 400; font-size: 30px; letter-spacing: 1.5px;
    text-transform: uppercase; color: var(--ink-light);
  }

  .contact-list {
    position: absolute; top: 170px; right: 30px;
    list-style: none; text-align: right; font-size: 13.5px; line-height: 1.35;
  }
  .contact-list li { display: flex; align-items: center; justify-content: flex-end; gap: 6px; }
  .contact-list svg { width: 10px; height: 10px; fill: var(--brand-red-bright); flex: none; }
  .contact-list .row--phone { font-size: 14.5px; }

  .address {
    position: absolute; left: 32px; bottom: 28px;
    font-size: 13.5px; line-height: 1.35;
  }

  .brand-mark {
    position: absolute; top: 96px; left: 0; width: 100%;
    display: flex; flex-direction: column; align-items: center; gap: 14px;
  }
  .brand-mark__circle {
    width: 58px; height: 58px; border-radius: 50%; background: var(--ink-light);
  }
  .brand-mark__name {
    font-weight: 600; font-size: 24px; letter-spacing: 1.5px;
    text-transform: uppercase; color: var(--ink-light);
  }
  .brand-url {
    position: absolute; bottom: 30px; left: 0; width: 100%;
    text-align: center; font-size: 14.5px;
  }
  .brand-url strong { font-weight: 700; }
</style>
</head>
<body>

  <section class="card card--contact" aria-label="Business card, contact side">
    <svg class="card__bands" viewBox="0 0 530 310" preserveAspectRatio="none" aria-hidden="true">
      <defs>
        <linearGradient id="blackTop" x1="0" y1="0" x2="0" y2="1">
          <stop offset="0" stop-color="#000"/>
          <stop offset="1" stop-color="#1e1e1e"/>
        </linearGradient>
        <linearGradient id="silverBand" x1="0" y1="0" x2="1" y2="0">
          <stop offset="0" stop-color="#8c8c8c"/>
          <stop offset="0.35" stop-color="#f2f2f2"/>
          <stop offset="1" stop-color="#9a9a9a"/>
        </linearGradient>
        <linearGradient id="redBottom" x1="0" y1="0" x2="0" y2="1">
          <stop offset="0" stop-color="#c01a22"/>
          <stop offset="1" stop-color="#6e0a10"/>
        </linearGradient>
      </defs>
      <rect width="530" height="310" fill="url(#blackTop)"/>
      <path d="M0 196 Q260 186 530 100 L530 310 L0 310 Z" fill="url(#silverBand)"/>
      <path d="M0 206 Q262 198 530 112 L530 310 L0 310 Z" fill="url(#redBottom)"/>
    </svg>

    <div class="holder">
      <p class="holder__name">Dorian T. Vickers</p>
      <p class="holder__title">C.E.O</p>
    </div>

    <div class="wordmark">
      <span class="wordmark__square" aria-hidden="true"></span>
      <span class="wordmark__name">K&amp;R Talent Collective</span>
    </div>

    <ul class="contact-list">
      <li class="row--phone">555-804-2917
        <svg viewBox="0 0 10 10" aria-hidden="true"><path d="M2 0.5 L4 2.8 L3 4 Q4.3 6 6 7 L7.2 6 L9.5 8 L8 9.6 Q3.5 9 0.4 2 Z"/></svg>
      </li>
      <li>dtvickers@krtalentcollective.example
        <svg viewBox="0 0 10 10" aria-hidden="true"><path d="M0.5 2 H9.5 V8 H0.5 Z M1 2.4 L5 5.6 L9 2.4" fill-rule="evenodd"/></svg>
      </li>
      <li>www.krtalentcollective.example
        <svg viewBox="0 0 10 10" aria-hidden="true"><circle cx="5" cy="5" r="4.5"/></svg>
      </li>
    </ul>

    <address class="address" style="font-style:normal">
      1187 Harrow Ridge Ave<br>
      Suite 410, Lakemont, OH 45900
    </address>
  </section>

  <section class="card card--brand" aria-label="Business card, brand side">
    <div class="brand-mark">
      <span class="brand-mark__circle" aria-hidden="true"></span>
      <span class="brand-mark__name">K&amp;R Talent Collective</span>
    </div>
    <p class="brand-url">www.<strong>krtalentcollective</strong>.example</p>
  </section>

</body>
</html>
```